Brackenfield Security Store Signage with provided LOGO

Need 2 designs (1) indicating the store is around the corner horizontal format and (1) in a vertical format without the around the corner indication. HD image for a 24" by 60" sign. Use attached image for inspiration. Our business of on the south side of a large building and we need to have 2 signs on the front of the build indicating LEFT and the last sign will be a sidewalk sign next to our business.
Updates

Project Deadline Extended
Reason: Allow a couple more designer to sumbit

Industry/Entity Type

Security

Font styles to use
Serif

Colors
33a6d7

Requirements
Must have
• WEBSITE URL: www.vaultwardstation.com and www.brackenfieldsecuritystore.com they can be in small font.
Nice to have
• Phone Number (855) 316-2984

```html
<!DOCTYPE html>
<html lang="en">
<head>
<meta charset="UTF-8">
<title>Brackenfield Security Store – Vertical Sign</title>
<link href="https://fonts.googleapis.com/css2?family=Anton&display=swap" rel="stylesheet">
<style>
  :root {
    --brand-blue: #329ef9;
    --brand-blue-light: #3ab3fb;
    --brand-blue-deep: #0a47f7;
    --paper: #ffffff;
    --trim: #2a2a2a;
  }
  html, body {
    margin: 0;
    padding: 0;
    width: 1200px;
    height: 3000px;
    overflow: hidden;
    background: var(--paper);
  }
  .sign {
    position: relative;
    width: 1200px;
    height: 3000px;
    background: var(--paper);
  }
  .sign-art {
    position: absolute;
    inset: 0;
    width: 1200px;
    height: 3000px;
    display: block;
  }
  .sign-text {
    font-family: 'Anton', 'Impact', sans-serif;
  }
</style>
</head>
<body>
<main class="sign">
  <svg class="sign-art" viewBox="0 0 1200 3000" xmlns="http://www.w3.org/2000/svg">
    <defs>
      <linearGradient id="headline-fade" x1="0" y1="0" x2="0" y2="1">
        <stop offset="0" stop-color="var(--brand-blue-light)"/>
        <stop offset="1" stop-color="var(--brand-blue-deep)"/>
      </linearGradient>
    </defs>

    <!-- trim line -->
    <rect class="trim" x="9.5" y="0.5" width="1190" height="2999" fill="none" stroke="var(--trim)" stroke-width="1.5"/>

    <!-- brand mark area -->
    <g class="brand-mark">
      <circle cx="600" cy="580" r="300" fill="var(--brand-blue)"/>
      <text class="sign-text brand-name" x="600" y="1080" text-anchor="middle"
            font-size="96" fill="var(--brand-blue)" letter-spacing="4">BRACKENFIELD</text>
    </g>

    <!-- framed name panel -->
    <g class="name-panel">
      <rect class="frame-outer" x="93" y="1330" width="1011" height="1297"
            fill="none" stroke="var(--brand-blue)" stroke-width="33"/>
      <rect class="frame-rule" x="120" y="1365" width="960" height="1227"
            fill="none" stroke="var(--brand-blue)" stroke-width="7"/>
      <rect class="frame-rule" x="131" y="1376" width="938" height="1205"
            fill="none" stroke="var(--brand-blue)" stroke-width="5"/>

      <text class="sign-text name-line name-line--first" x="158" y="1686"
            font-size="250" fill="url(#headline-fade)"
            textLength="884" lengthAdjust="spacingAndGlyphs">BRACKENFIELD</text>
      <text class="sign-text name-line" x="170" y="2022"
            font-size="300" fill="var(--brand-blue)"
            textLength="862" lengthAdjust="spacingAndGlyphs">SECURITY</text>
      <text class="sign-text name-line" x="165" y="2493"
            font-size="470" fill="var(--brand-blue)"
            textLength="870" lengthAdjust="spacingAndGlyphs">STORE</text>
    </g>
  </svg>
</main>
</body>
</html>
```